Dentist's Office needs desktop and mobile website design

This is a turnkey project where we are looking for a bright, elegant, modern website design, both for desktop and mobile. Our existing website is hosted on Google sites. We also require the new design to be set up and fully functional - both desktop and mobile - on Google sites. If Google sites is too limiting, its ok to use a platform like Wix or Squarespace. If using these, we will need you to point our domain to the new Wix site, and hand us the credentials so we can continue to update the site.

We want to continue using our current logo so the new website colors need to go with the logo. Our existing website can be found at www.smilebay47.com.

We want the new website to have the following pages:
1. Home - similar content to our current home page at http://www.smilebay47.com

We also have pictures of our office and team that we would like to show up on the home page in a collage, slide show, or some other creative. Pictures can be found here: https://files.exampleshare.net/folderview?id=7KQ2MVRAXPL4hYwnBzTcLdEgHsJu&usp=sharing

Not all pictures have to be used; use as many as needed.

In addition to the content on our current home page, we would like a small section for dental quotes where we could rotate quotes. Sample quotes can be found at http://www.sayingsmeadow.net/dental.html

If above content is too much to fit on one page, it is ok to split into two.

2. Our team - similar to http://www.smilebay47.com/our-dentist-1 . In addition, we want short bios and pictures of other staff added to this page. Pictures and bios can be found here: https://files.exampleshare.net/folderview?id=7KQ2MVRAXPL4hYwnBzTcLdEgHsJu&usp=sharing

3. Reviews - similar to http://www.smilebay47.com/patient-testimonials-1

4. Services - provide a summary of services we provide from http://www.smilebay47.com/dental-services . No need for detailed pages pages for each treatment we have on our current website.

5. Contact Us - http://www.smilebay47.com/contact-us

Target Market(s)

local population

Industry/Entity Type

Healthcare

Coding

Coded - Design and coding required

Number of Pages Required

5+ page

Font styles to use
Sans Serif

Requirements
Nice to have
• animated icons would be cool

```html
<!DOCTYPE html>
<html lang="en">
<head>
<meta charset="utf-8">
<title>Sunvale Dental Care</title>
<link rel="stylesheet" href="https://fonts.googleapis.com/css2?family=Raleway:wght@400;500;600&display=swap">
<style>
:root{
  --orange:#ee8d34;
  --orange-dark:#e47f28;
  --green:#7cbb52;
  --ink:#444;
  --grey:#e4e4e4;
  --rule:#ddd;
  --white:#fff;
}
*{box-sizing:border-box;margin:0;padding:0}
html,body{width:694px;height:1200px;overflow:hidden;background:var(--white)}
body{position:relative;font-family:"Raleway",sans-serif;color:var(--ink)}
.abs{position:absolute}
.top-line{left:0;top:0;width:694px;height:2px;background:var(--orange)}
.brand{display:flex;align-items:center;justify-content:center;background:var(--orange);color:var(--white);border-radius:16px;font-weight:400;white-space:nowrap;overflow:hidden}
.header-brand{left:56px;top:11px;width:94px;height:30px;font-size:8.6px}
.contact-top{font-size:7px;color:var(--ink);display:flex;gap:6px;align-items:flex-start;line-height:12px}
.contact-top svg{flex:none}
.divider-v{left:475px;top:18px;width:1px;height:22px;background:var(--rule)}
.nav{left:0;top:59px;width:694px;height:33px;background:var(--orange)}
.nav a{position:absolute;top:12px;font-size:7px;color:var(--white);text-decoration:none}
.nav .sep{position:absolute;top:9px;width:1px;height:15px;background:rgba(255,255,255,.25)}
.search{left:602px;top:8px;width:28px;height:18px;border-radius:9px;background:var(--white);display:flex;align-items:center;justify-content:center}
.hero{left:0;top:92px;width:694px;height:298px;border-radius:0 0 24px 24px;overflow:hidden;background:linear-gradient(180deg,#b9aea3 0%,#a18c78 45%,#7e6a59 100%)}
.hero .quote{position:absolute;left:0;width:694px;top:236px;text-align:center;color:var(--white);font-size:18.5px;line-height:26px;font-weight:500}
.hero .arrow{position:absolute;top:110px}
.welcome{left:0;top:417px;width:694px;text-align:center;font-size:15.5px;font-weight:600;color:var(--orange)}
.welcome .g{color:var(--green)}
.intro{left:84px;top:453px;width:526px;text-align:center;font-size:6.8px;line-height:17.5px}
.card{top:550px;width:137px;height:235px}
.card .box{position:absolute;left:0;top:66px;width:137px;height:169px;border-radius:3px;color:var(--white);text-align:center}
.card.o .box{background:var(--orange)}
.card.g .box{background:var(--green)}
.card .photo{position:absolute;left:7px;top:0;width:124px;height:124px;border-radius:50%;border:4px solid var(--white)}
.card.o .photo{background:radial-gradient(circle at 50% 45%,#c89878 0%,#e89a3e 55%,#f0a848 100%)}
.card.g .photo{background:radial-gradient(circle at 50% 45%,#c6a08a 0%,#b9b6ad 60%,#d2cfc6 100%)}
.card h3{position:absolute;top:76px;width:100%;font-size:10px;font-weight:500}
.card p{position:absolute;top:94px;left:10px;right:10px;font-size:6.8px;line-height:14.5px}
.card a{position:absolute;top:142px;left:0;width:100%;font-size:7.5px;color:var(--white);text-decoration:underline}
.rule{left:57px;top:815px;width:580px;height:1px;background:var(--orange)}
.section-title{top:838px;font-size:14px;font-weight:600;color:var(--orange)}
.section-title .g{color:var(--green)}
.quote-box{left:57px;top:882px;width:261px;height:66px;background:var(--grey);font-size:7.5px;line-height:15px;padding:10px 24px 0 37px}
.quote-box .by{position:absolute;right:22px;top:42px;font-weight:500;font-size:8px;color:#333}
.quote-mark{left:70px;top:887px;font-size:14px;color:#bbb;font-weight:600}
.avatar{left:68px;top:928px;width:64px;height:64px;border-radius:50%;border:4px solid var(--white);box-shadow:0 1px 4px rgba(0,0,0,.25);background:radial-gradient(circle at 50% 45%,#c8a088 0%,#7c6d9e 70%)}
.quote-name{left:145px;top:963px;font-size:10px;color:var(--green)}
.col-rule{left:338px;top:865px;width:1px;height:120px;background:#eee}
.members-text{left:357px;top:874px;width:280px;font-size:6.8px;line-height:16px;color:#666}
.badge{top:937px;height:35px;border-radius:17px;border:1px solid #e2e2e2;box-shadow:0 1px 3px rgba(0,0,0,.12);background:var(--white);display:flex;align-items:center;justify-content:center}
.badge span{display:block;height:10px;border-radius:2px}
.footer{left:0;top:1015px;width:694px;height:143px;background:#ef9040}
.footer-brand{left:58px;top:45px;width:128px;height:44px;font-size:11.5px;border-radius:22px;background:#f4a35a}
.footer h4{position:absolute;top:25px;font-size:8px;font-weight:400;color:var(--white);letter-spacing:.3px}
.footer ul{position:absolute;top:47px;list-style:none;font-size:6.8px;color:var(--white)}
.footer li{height:16px}
.footer li::before{content:"»";margin-right:7px}
.footer .ci{position:absolute;font-size:6.8px;color:var(--white);line-height:13px;display:flex;gap:9px}
.copy{left:0;top:1158px;width:694px;height:42px;background:var(--orange-dark);text-align:center;color:var(--white);font-size:6.8px;line-height:42px}
</style>
</head>
<body>
<div class="abs top-line"></div>
<div class="abs brand header-brand">Sunvale dental care</div>
<div class="abs contact-top" style="left:390px;top:19px">
  <svg width="7" height="10" viewBox="0 0 7 10"><rect x=".5" y=".5" width="6" height="9" rx="1" fill="none" stroke="#ee8d34"/><rect x="2.5" y="7.5" width="2" height="1" fill="#ee8d34"/></svg>
  <span>- &nbsp;209-555-0184</span>
</div>
<div class="abs divider-v"></div>
<div class="abs contact-top" style="left:491px;top:19px">
  <svg width="8" height="11" viewBox="0 0 8 11"><path d="M4 0a4 4 0 0 0-4 4c0 3 4 7 4 7s4-4 4-7a4 4 0 0 0-4-4z" fill="#ee8d34"/><circle cx="4" cy="4" r="1.5" fill="#fff"/></svg>
  <span>- &nbsp;4820 W Orchard Ave, Lindale , CA 95301<br>&nbsp;&nbsp;(next to Casa Verde Market)</span>
</div>

<nav class="abs nav">
  <a style="left:57px">Home</a><span class="sep" style="left:121px"></span>
  <a style="left:164px">Our Team</a><span class="sep" style="left:242px"></span>
  <a style="left:281px">Reviews</a><span class="sep" style="left:357px"></span>
  <a style="left:395px">Services</a><span class="sep" style="left:471px"></span>
  <a style="left:510px">Contact Us</a>
  <span class="abs search"><svg width="9" height="9" viewBox="0 0 9 9"><circle cx="3.7" cy="3.7" r="2.7" fill="none" stroke="#ee8d34" stroke-width="1.4"/><line x1="5.7" y1="5.7" x2="8.3" y2="8.3" stroke="#ee8d34" stroke-width="1.6"/></svg></span>
</nav>

<section class="abs hero" role="img" aria-label="Photo of the dental team chatting with a patient at the reception desk">
  <svg class="arrow" style="left:30px" width="8" height="12" viewBox="0 0 8 12"><path d="M6 1 1 6l5 5" fill="none" stroke="#fff" stroke-width="1.6"/></svg>
  <svg class="arrow" style="left:654px" width="8" height="12" viewBox="0 0 8 12"><path d="M2 1l5 5-5 5" fill="none" stroke="#fff" stroke-width="1.6"/></svg>
  <p class="quote">“ Every tooth in a man’s head is more<br>valuable than a diamond ”</p>
</section>

<h1 class="abs welcome">Welcome To <span class="g">Sunvale</span> dental Care</h1>
<p class="abs intro">We want to provide you with everything you could want in a dental office: excellent work, a gentle nature, and a friendly staff - all in a comfortable location and at a great price. Dr Maren, our dentist, combines many years of experience in the dental field, with her gentle and friendly personality. Over the course of her career, she has also worked with several Oral &amp; Maxillofacial Surgeons. Her experience enables her to excel at complex procedures that many dentists must refer out to other offices. If you have insurance, we are most likely a preferred provider. We also offer financing options.</p>

<article class="abs card o" style="left:57px">
  <div class="box"><h3>Lena Morcos</h3><p>Lena attended RVC in Hanford, CA. He has been practicing . Dental Hy-giene since 2009.</p><a>More Info</a></div>
  <div class="photo" role="img" aria-label="Portrait of Lena Morcos"></div>
</article>
<article class="abs card g" style="left:205px">
  <div class="box"><h3>Dario Velez</h3><p>It brings Dario great pleasure to be a part of a dental team. Itsher passion to help patients love their smile</p><a>More Info</a></div>
  <div class="photo" role="img" aria-label="Portrait of Dario Velez"></div>
</article>
<article class="abs card o" style="left:352px">
  <div class="box"><h3>Tessa Rowan</h3><p>Tessa attended RVC in Hanford, CA. He has been practicing . Dental Hy-giene since 2009.</p><a>More Info</a></div>
  <div class="photo" role="img" aria-label="Portrait of Tessa Rowan"></div>
</article>
<article class="abs card g" style="left:500px">
  <div class="box"><h3>Lena Morcos</h3><p>Lena attended RVC in Hanford, CA. He has been practicing . Dental Hy-giene since 2009.</p><a>More Info</a></div>
  <div class="photo" role="img" aria-label="Portrait of Dr Maren"></div>
</article>

<div class="abs rule"></div>

<h2 class="abs section-title" style="left:56px">Dental <span class="g">Quotes</span></h2>
<div class="abs quote-box">The toothbrush doesn't remove six months of tartar 30 minutes before your appointment<span class="abs by">Dental Saying</span></div>
<div class="abs quote-mark">“</div>
<div class="abs avatar" role="img" aria-label="Portrait of the quote author"></div>
<div class="abs quote-name">Scriptorem ei usu</div>

<div class="abs col-rule"></div>
<h2 class="abs section-title" style="left:356px">Members <span class="g">of</span></h2>
<p class="abs members-text">Nullam mollis facilis eam at. Per legendos adipiscing in. Case lucilius erroribus qui et, solet legendos no vim. Incorrupte omittantur sea ex. Nullam mollis facilis eam at. Per legendos adipiscing in. Case lucilius erroribus qui et, solet legendos no vim.</p>
<div class="abs badge" style="left:357px;width:93px" role="img" aria-label="Dental association membership badge"><span style="width:58px;background:var(--green)"></span></div>
<div class="abs badge" style="left:453px;width:89px" role="img" aria-label="State dental association membership badge"><span style="width:40px;height:18px;background:#999"></span></div>
<div class="abs badge" style="left:547px;width:90px" role="img" aria-label="Regional dental society membership badge"><span style="width:40px;height:16px;background:#8aa0b8"></span></div>

<footer class="abs footer">
  <div class="abs brand footer-brand">Sunvale dental care</div>
  <h4 style="left:216px">MENUS</h4>
  <ul style="left:216px"><li>Home</li><li>About us</li><li>Our services</li><li>Blog</li><li>Contact us</li></ul>
  <h4 style="left:295px">QUICK LINKS</h4>
  <ul style="left:295px"><li>Site map</li><li>Terms and Conditions</li><li>Disclaimer</li><li>Privacy Policy</li><li>Contact us</li></ul>
  <h4 style="left:403px">CONTACT US</h4>
  <div class="ci" style="left:403px;top:46px"><svg width="9" height="8" viewBox="0 0 9 8"><path d="M4.5 0 0 4h1.3v4h2.4V5.5h1.6V8h2.4V4H9z" fill="#fff"/></svg><span>2270 Elm Park Rd | Fairview<br>KS 66099</span></div>
  <div class="ci" style="left:405px;top:89px"><svg width="6" height="9" viewBox="0 0 6 9"><rect x=".5" y=".5" width="5" height="8" rx="1" fill="none" stroke="#fff"/></svg><span>Call Us : (913)555-0142</span></div>
  <div class="ci" style="left:403px;top:113px"><svg width="10" height="7" viewBox="0 0 10 7"><rect x=".5" y=".5" width="9" height="6" fill="none" stroke="#fff"/><path d="M.5.5 5 4l4.5-3.5" fill="none" stroke="#fff"/></svg><span>info@sunvaledental.com</span></div>
  <h4 style="left:533px">CONNECT US WITH</h4>
  <svg class="abs" style="left:532px;top:62px" width="106" height="24" viewBox="0 0 106 24">
    <g fill="none" stroke="#fff" stroke-width="1.4"><circle cx="12" cy="12" r="10.5"/><circle cx="39.5" cy="12" r="10.5"/><circle cx="67" cy="12" r="10.5"/><circle cx="94" cy="12" r="10.5"/></g>
  </svg>
</footer>
<div class="abs copy">© &nbsp;Sunvale Dental 2016 . All Rights Reserved</div>
</body>
</html>
```